Stylish Homeware business needs a Logo and Business Card design

We need a logo and business card for a new company based in Hong Kong called "Nest Lumora". We do marketing and distributing international stylish Homeware brands in Asia. Products we handle included clocks, picture frame, small kitchen wares, LED lightenings, stationary and etc. We planned to also create our own brands next step. We could like to see designs that use pastel colors. The final design shoudl be simple and stylish.
Target Market(s)
Asia, Mainly Japan, China and Korea
Industry/Entity Type
Business
Contact Information for Business Card
We could like to see designs that use pastel colors. The final design shoudl be simple and stylish. We attach some log design we like on the bottom of the page.
Font styles to use
Look and feel
Each slider illustrates characteristics of the customer's brand and the style your logo design should communicate.

```html
<!DOCTYPE html>
<html lang="en">
<head>
<meta charset="utf-8">
<title>Nest Lumora — Business Card</title>
<link rel="stylesheet" href="https://fonts.googleapis.com/css2?family=Arvo:wght@400;700&family=Lora:wght@400&display=swap">
<style>
  :root {
    --stage: #e9ecf1;
    --card: #fbf7f2;
    --card-glow: #fffdf9;
    --band-peach: #f4c9b6;
    --band-rose: #f2d6df;
    --band-lilac: #d9d3ee;
    --band-mint: #cde9dc;
    --ink: #4f5468;
    --ink-soft: #6e7388;
    --accent: #c7918b;
  }
  * { box-sizing: border-box; margin: 0; padding: 0; }
  html, body { width: 1200px; height: 800px; overflow: hidden; }
  body {
    background: var(--stage);
    display: flex;
    align-items: center;
    justify-content: center;
    gap: 60px;
  }
  .card {
    position: relative;
    width: 525px;
    height: 300px;
    background: radial-gradient(ellipse at 55% 40%, var(--card-glow), var(--card) 75%);
    overflow: hidden;
    box-shadow: 0 18px 40px rgba(79, 84, 104, .18);
  }
  .card__bands { position: absolute; inset: 0; width: 100%; height: 100%; }

  /* brand side */
  .brand {
    position: absolute;
    inset: 0;
    display: flex;
    flex-direction: column;
    align-items: center;
    justify-content: center;
    gap: 14px;
  }
  .brand__ring {
    width: 74px; height: 74px;
    border-radius: 50%;
    border: 5px solid var(--accent);
  }
  .brand__name {
    font-family: "Arvo", serif;
    font-weight: 400;
    font-size: 26px;
    letter-spacing: 4px;
    color: var(--ink);
    text-transform: uppercase;
  }

  /* contact side */
  .person {
    position: absolute;
    top: 74px;
    left: 0; right: 0;
    text-align: center;
    color: var(--ink);
  }
  .person__name {
    font-family: "Arvo", serif;
    font-weight: 700;
    font-size: 25px;
    letter-spacing: 1.5px;
  }
  .person__role {
    font-family: "Arvo", serif;
    font-weight: 700;
    font-size: 10px;
    letter-spacing: 2px;
    margin-top: 3px;
    color: var(--accent);
  }
  .contacts {
    position: absolute;
    top: 136px;
    left: 0; right: 0;
    display: grid;
    grid-template-columns: 1fr 24px 1fr;
    align-items: center;
    font-family: "Lora", serif;
    font-size: 12.5px;
    color: var(--ink-soft);
  }
  .contacts__col { display: flex; flex-direction: column; gap: 10px; }
  .contacts__col--left { align-items: flex-end; }
  .contacts__col--right { align-items: flex-start; }
  .contact { display: flex; align-items: center; gap: 8px; }
  .divider {
    justify-self: center;
    width: 1px; height: 44px;
    background: var(--accent);
    transform: rotate(18deg);
  }
  .icon { width: 22px; height: 22px; flex: none; }
  .address {
    position: absolute;
    top: 208px;
    left: 0; right: 0;
    display: flex;
    justify-content: center;
    align-items: center;
    gap: 10px;
    font-family: "Lora", serif;
    font-size: 12.5px;
    color: var(--ink-soft);
  }
</style>
</head>
<body>

<svg width="0" height="0" style="position:absolute">
  <defs>
    <linearGradient id="pastel-band" x1="0" y1="0" x2="1" y2="0">
      <stop offset="0" stop-color="#f4c9b6"/>
      <stop offset="0.35" stop-color="#f2d6df"/>
      <stop offset="0.65" stop-color="#d9d3ee"/>
      <stop offset="1" stop-color="#cde9dc"/>
    </linearGradient>
  </defs>
</svg>

<section class="card card--front" aria-label="Business card front">
  <svg class="card__bands" viewBox="0 0 525 300" preserveAspectRatio="none" aria-hidden="true">
    <path d="M150 0 H525 V14 Q330 20 150 0 Z" fill="url(#pastel-band)"/>
    <path d="M0 268 Q200 260 380 300 H0 Z" fill="url(#pastel-band)"/>
  </svg>

  <div class="person">
    <h1 class="person__name">ADRIAN VALE</h1>
    <p class="person__role">GENERAL DIRECTOR</p>
  </div>

  <div class="contacts">
    <div class="contacts__col contacts__col--left">
      <div class="contact">
        <span>+1 555 014 270</span>
        <svg class="icon" viewBox="0 0 22 22" aria-hidden="true">
          <circle cx="11" cy="11" r="10" fill="none" stroke="var(--accent)" stroke-width="1.2"/>
          <path d="M8 6.5l1.6-.4 1 2.3-1 .8q.8 1.8 2.2 2.6l.9-.9 2.2 1.1-.4 1.6q-3 .4-5-2.2T8 6.5z" fill="var(--accent)"/>
        </svg>
      </div>
      <div class="contact">
        <span>info@nestlumora.com</span>
        <svg class="icon" viewBox="0 0 22 22" aria-hidden="true">
          <circle cx="11" cy="11" r="10" fill="none" stroke="var(--accent)" stroke-width="1.2"/>
          <rect x="6" y="7.5" width="10" height="7" fill="none" stroke="var(--accent)" stroke-width="1.1"/>
          <path d="M6 7.5l5 4 5-4" fill="none" stroke="var(--accent)" stroke-width="1.1"/>
        </svg>
      </div>
    </div>

    <span class="divider" aria-hidden="true"></span>

    <div class="contacts__col contacts__col--right">
      <div class="contact">
        <svg class="icon" viewBox="0 0 22 22" aria-hidden="true">
          <circle cx="11" cy="11" r="10" fill="none" stroke="var(--accent)" stroke-width="1.2"/>
          <rect x="8" y="5.5" width="6" height="11" rx="1" fill="none" stroke="var(--accent)" stroke-width="1.1"/>
          <circle cx="11" cy="14.6" r=".7" fill="var(--accent)"/>
        </svg>
        <span>+1 555 014 270</span>
      </div>
      <div class="contact">
        <svg class="icon" viewBox="0 0 22 22" aria-hidden="true">
          <circle cx="11" cy="11" r="10" fill="none" stroke="var(--accent)" stroke-width="1.2"/>
          <circle cx="11" cy="11" r="5" fill="none" stroke="var(--accent)" stroke-width="1.1"/>
          <path d="M6 11h10M11 6q-2.5 5 0 10M11 6q2.5 5 0 10" fill="none" stroke="var(--accent)" stroke-width=".9"/>
        </svg>
        <span>www.nestlumora.com</span>
      </div>
    </div>
  </div>

  <div class="address">
    <svg class="icon" viewBox="0 0 22 22" aria-hidden="true">
      <circle cx="11" cy="11" r="10.5" fill="var(--accent)"/>
      <path d="M11 5.5a3.6 3.6 0 0 0-3.6 3.6c0 2.7 3.6 6.4 3.6 6.4s3.6-3.7 3.6-6.4A3.6 3.6 0 0 0 11 5.5z" fill="var(--card)"/>
      <circle cx="11" cy="9.1" r="1.3" fill="var(--accent)"/>
    </svg>
    <span>88 Harbour Road, Wan Chai, Hong Kong, 000000.</span>
  </div>
</section>

<section class="card card--back" aria-label="Business card back">
  <svg class="card__bands" viewBox="0 0 525 300" preserveAspectRatio="none" aria-hidden="true">
    <path d="M0 0 H525 V8 Q260 14 0 4 Z" fill="url(#pastel-band)"/>
    <path d="M0 290 Q260 284 525 292 V300 H0 Z" fill="url(#pastel-band)"/>
  </svg>
  <div class="brand">
    <span class="brand__ring" aria-hidden="true"></span>
    <span class="brand__name">Nest Lumora</span>
  </div>
</section>

</body>
</html>
```